co working space / serviced office/ business centre

Brivlo - brivlo.in, is a very young brand bieng run by 3 young entrepreneurs. We want to be become out of the league company delivering fabulous and beautiful serviced offices in India and abroad. We hire designers who have made spaces across the world. We want to get visiting card design which gives complete fresh look to the people who carries that card, has to be very impactful and should symbolise happy young and energetic brand. should be completely out of the box thinking of international level, should portray global brand image.

Target Market(s)

Startups, (Small, medium and large corporates)

Industry/Entity Type

Business

Contact Information for Business Card

Name, Email, Address, Mobile number, Landline number, website

Colors

Designer to choose colors to be used in the design.

Requirements
Must have
• Nice new shape
Nice to have
• We want creative cuts, different size and impactful brand clarity
Should not have
• Boring and regular design and shape

```html
<!DOCTYPE html>
<html lang="en">
<head>
<meta charset="utf-8">
<title>Brivlo Business Card</title>
<link rel="stylesheet" href="https://fonts.googleapis.com/css2?family=Orbitron:wght@500;700&family=Lato:wght@400;700&display=swap">
<style>
  :root {
    --bg: #e6e6e6;
    --card: #1c1d1f;
    --edge: #0d0d0e;
    --red: #e8202a;
    --white: #f2f2f2;
  }
  * { margin: 0; padding: 0; box-sizing: border-box; }
  html, body { width: 1200px; height: 675px; overflow: hidden; }
  body { background: var(--bg); position: relative; font-family: "Lato", sans-serif; }

  .card {
    position: absolute;
    top: 198px;
    width: 500px;
    height: 284px;
    background: var(--card);
    border: 4px solid var(--edge);
    border-radius: 44px;
  }
  .card--front { left: 62px; }
  .card--back { left: 602px; }
  .card__frame {
    position: absolute;
    inset: 1px;
    border: 3px solid var(--red);
    border-radius: 40px;
  }
  .card__item {
    position: absolute;
    left: 0;
    right: 0;
    margin: 0 auto;
    text-align: center;
    color: var(--red);
    font-family: "Orbitron", sans-serif;
    line-height: 1;
  }

  /* front */
  .brand-mark { top: 74px; font-size: 24px; font-weight: 700; letter-spacing: 2px; }
  .person__name { top: 131px; font-size: 19px; font-weight: 700; letter-spacing: 1px; }
  .person__rule { top: 155px; width: 174px; height: 3px; background: var(--red); }
  .person__role { top: 164px; font-size: 11px; font-weight: 500; letter-spacing: 1.5px; }
  .contact {
    top: 190px;
    font-family: "Lato", sans-serif;
    font-style: normal;
    color: var(--white);
    font-size: 13px;
    line-height: 17px;
  }
  .contact__label { color: var(--red); font-weight: 700; }

  /* back */
  .brand-dot {
    top: 50px;
    width: 70px;
    height: 70px;
    border: 9px solid var(--red);
    border-radius: 50%;
  }
  .brand-name { top: 134px; font-size: 45px; font-weight: 700; letter-spacing: 1px; }
  .brand-rule { top: 189px; width: 276px; height: 3px; background: var(--red); }
  .brand-tagline { top: 205px; font-size: 13px; font-weight: 700; letter-spacing: 3px; }
</style>
</head>
<body>
  <section class="card card--front" aria-label="Business card front">
    <div class="card__frame"></div>
    <div class="card__item brand-mark">BRIVLO</div>
    <h1 class="card__item person__name">ROHAN VEDANSHI</h1>
    <div class="card__item person__rule"></div>
    <p class="card__item person__role">CEO/FOUNDER</p>
    <address class="card__item contact">
      <div>Tower 4C, Lake Park, Noida</div>
      <div><span class="contact__label">P</span>: +91 8000123456 <span class="contact__label">C</span>: +91 9000654321</div>
      <div><span class="contact__label">E</span>: rohan@brivlo.in <span class="contact__label">W</span>: www.brivlo.in</div>
    </address>
  </section>

  <section class="card card--back" aria-label="Business card back">
    <div class="card__frame"></div>
    <div class="card__item brand-dot"></div>
    <div class="card__item brand-name">BRIVLO</div>
    <div class="card__item brand-rule"></div>
    <p class="card__item brand-tagline">PLUG. PLAN. GROW</p>
  </section>
</body>
</html>
```